Core Values Poster for Technology Business

A core values poster for our office. We don't have much in mind beyond a couple of logos (we have two companies) and then the 4 Core Values we want to present. Mostly, we want this to be simple (easy to take in as a reminder in 5-10 seconds) in a very visually appealing way.

If you can incorporate a high-look-and-feel, great, but not if it over complicates the entire poster/sign.

The core values are:
Relationships Matter
Passion Drives us to Excellence
All About Teamwork
Consistent, Resourceful, Relentless

Our file with both logos together is attached. This is a low-res version. We would provide a high-res version for final production.

Industry/Entity Type

Business

Font styles to use
Serif

Colors
ec1f27
0255a3

Requirements
Nice to have
• This is an update. To be able to incorporate some of our corporate look-and-feel, but not have a black background (as on our plovarix.com stie), please see the Video Conferencing Slick file that I have uploaded. Might be able to use parts of this type of format to tie in (but not use it exactly as-is - since this is a client facing document).

```html
<!DOCTYPE html>
<html lang="en">
<head>
<meta charset="utf-8">
<title>Core Values Posters</title>
<link rel="stylesheet" href="https://fonts.googleapis.com/css2?family=Bebas+Neue&display=swap">
<style>
  :root {
    --page: #ffffff;
    --night: #0f0f12;
    --red: #e5305a;
    --blue: #3a7fb1;
    --gold: #f3e7a4;
    --ink: #222222;
    --white: #ffffff;
  }
  * { box-sizing: border-box; margin: 0; padding: 0; }
  html, body { width: 1200px; height: 1000px; overflow: hidden; background: var(--page); }
  body { position: relative; font-family: "Bebas Neue", "Arial Narrow", sans-serif; }

  .poster {
    position: absolute; top: 100px; width: 570px; height: 858px; overflow: hidden;
    background: linear-gradient(180deg, var(--white) 0, var(--white) 90px, #8a8a8e 125px, var(--night) 165px, var(--night) 100%);
  }
  .poster--light { left: 22px; }
  .poster--dark { left: 614px; }

  .poster__bands { position: absolute; inset: 0; width: 570px; height: 858px; }

  .brand { position: absolute; color: var(--ink); font-size: 22px; line-height: 1; letter-spacing: 1px; }
  .brand--left { left: 16px; top: 30px; display: flex; align-items: center; gap: 8px; }
  .brand--right { right: 22px; top: 16px; display: flex; align-items: center; gap: 8px; }
  .brand__mark { width: 16px; height: 16px; border-radius: 50%; background: var(--red); flex: none; }
  .brand__name { display: block; }

  .value { position: absolute; line-height: 0.9; white-space: nowrap; transform-origin: left top; }
  .poster--light .value--red { color: var(--red); }
  .poster--light .value--blue { color: var(--blue); }
  .poster--dark .value { color: var(--white); }

  .relationships { left: 138px; top: 300px; font-size: 83px; transform: scaleY(1.12); }
  .matter { left: 140px; top: 375px; font-size: 32px; letter-spacing: 22px; }
  .passion { left: 52px; top: 418px; font-size: 46px; letter-spacing: 1px; }
  .excellence { left: 50px; top: 452px; font-size: 88px; letter-spacing: 2px; }
  .all-about { left: 168px; top: 538px; font-size: 40px; letter-spacing: 18px; }
  .teamwork { left: 166px; top: 570px; font-size: 88px; letter-spacing: 2px; }
  .trio { left: 64px; top: 656px; font-size: 68px; line-height: 0.82; letter-spacing: 1px; }

  .icon { position: absolute; border-radius: 8px; }
  .poster--light .icon { background: var(--red); }
  .poster--light .icon--blue { background: var(--blue); }
  .poster--dark .icon { background: var(--white); }
  .icon--handshake { left: 38px; top: 322px; width: 90px; height: 66px; }
  .icon--trophy { left: 434px; top: 426px; width: 78px; height: 88px; }
  .icon--team { left: 50px; top: 530px; width: 106px; height: 114px; }

  .network { position: absolute; left: 378px; top: 668px; width: 160px; height: 142px; }
  .network line { stroke-width: 4; }
  .poster--light .network line, .poster--light .network .node { stroke: var(--blue); }
  .poster--dark .network line, .poster--dark .network .node { stroke: var(--white); }
  .network .node { fill: none; stroke-width: 4; }
  .poster--light .network .node-fill { fill: var(--blue); }
  .poster--dark .network .node-fill { fill: var(--white); }
</style>
</head>
<body>

<section class="poster poster--light">
  <svg class="poster__bands" viewBox="0 0 570 858">
    <path d="M0,112 Q285,52 570,112 L570,138 Q285,78 0,138 Z" fill="var(--red)"/>
    <path d="M0,148 Q285,90 570,148 L570,236 Q285,188 0,236 Z" fill="var(--blue)"/>
    <path d="M0,248 Q285,194 570,248 L570,284 Q285,230 0,284 Z" fill="var(--red)"/>
    <path d="M26,300 Q287,232 548,300 L548,832 L26,832 Z" fill="var(--white)" stroke="var(--red)" stroke-width="4"/>
    <circle cx="92" cy="194" r="8" fill="var(--gold)"/>
    <circle cx="478" cy="194" r="8" fill="var(--gold)"/>
    <path id="arcL" d="M110,212 Q285,160 460,212" fill="none"/>
    <text font-family="'Bebas Neue', sans-serif" font-size="80" fill="var(--white)" letter-spacing="3" text-anchor="middle">
      <textPath href="#arcL" startOffset="50%">Core Values</textPath>
    </text>
  </svg>

  <div class="brand brand--left"><span class="brand__mark"></span><span class="brand__name">Corvalen<br>Technology Solutions</span></div>
  <div class="brand brand--right"><span class="brand__name">Harwick<br>Security<br>Group</span></div>

  <div class="icon icon--handshake" role="img" aria-label="Handshake icon"></div>
  <div class="value value--red relationships">Relationships</div>
  <div class="value value--red matter">Matter</div>

  <div class="value value--blue passion">Passion Drives us to</div>
  <div class="value value--blue excellence">Excellence</div>
  <div class="icon icon--blue icon--trophy" role="img" aria-label="Trophy held in a hand icon"></div>

  <div class="icon icon--team" role="img" aria-label="Two teammates raising a trophy icon"></div>
  <div class="value value--red all-about">All About</div>
  <div class="value value--red teamwork">Teamwork</div>

  <div class="value value--blue trio">Consistent<br>Resourceful<br>Relentless</div>
  <svg class="network" viewBox="0 0 160 142" role="img" aria-label="Connected circles for team, growth and process">
    <line x1="55" y1="60" x2="100" y2="42"/>
    <line x1="55" y1="80" x2="82" y2="105"/>
    <circle class="node" cx="32" cy="70" r="28"/>
    <circle class="node-fill" cx="32" cy="70" r="16"/>
    <circle class="node" cx="126" cy="32" r="28"/>
    <circle class="node-fill" cx="126" cy="32" r="12"/>
    <circle class="node" cx="102" cy="112" r="28"/>
    <circle class="node-fill" cx="102" cy="112" r="12"/>
  </svg>
</section>

<section class="poster poster--dark">
  <svg class="poster__bands" viewBox="0 0 570 858">
    <path d="M0,112 Q285,52 570,112 L570,138 Q285,78 0,138 Z" fill="var(--red)"/>
    <path d="M0,148 Q285,90 570,148 L570,236 Q285,188 0,236 Z" fill="var(--blue)"/>
    <path d="M0,248 Q285,194 570,248 L570,284 Q285,230 0,284 Z" fill="var(--red)"/>
    <circle cx="92" cy="194" r="8" fill="var(--gold)"/>
    <circle cx="478" cy="194" r="8" fill="var(--gold)"/>
    <path id="arcR" d="M110,212 Q285,160 460,212" fill="none"/>
    <text font-family="'Bebas Neue', sans-serif" font-size="80" fill="var(--white)" letter-spacing="3" text-anchor="middle">
      <textPath href="#arcR" startOffset="50%">Core Values</textPath>
    </text>
  </svg>

  <div class="brand brand--left"><span class="brand__mark"></span><span class="brand__name">Corvalen<br>Technology Solutions</span></div>
  <div class="brand brand--right"><span class="brand__name">Harwick<br>Security<br>Group</span></div>

  <div class="icon icon--handshake" role="img" aria-label="Handshake icon"></div>
  <div class="value relationships">Relationships</div>
  <div class="value matter">Matter</div>

  <div class="value passion">Passion Drives us to</div>
  <div class="value excellence">Excellence</div>
  <div class="icon icon--trophy" role="img" aria-label="Trophy held in a hand icon"></div>

  <div class="icon icon--team" role="img" aria-label="Two teammates raising a trophy icon"></div>
  <div class="value all-about">All About</div>
  <div class="value teamwork">Teamwork</div>

  <div class="value trio">Consistent<br>Resourceful<br>Relentless</div>
  <svg class="network" viewBox="0 0 160 142" role="img" aria-label="Connected circles for team, growth and process">
    <line x1="55" y1="60" x2="100" y2="42"/>
    <line x1="55" y1="80" x2="82" y2="105"/>
    <circle class="node" cx="32" cy="70" r="28"/>
    <circle class="node-fill" cx="32" cy="70" r="16"/>
    <circle class="node" cx="126" cy="32" r="28"/>
    <circle class="node-fill" cx="126" cy="32" r="12"/>
    <circle class="node" cx="102" cy="112" r="28"/>
    <circle class="node-fill" cx="102" cy="112" r="12"/>
  </svg>
</section>

</body>
</html>
```